Brochure for The Harbourline Group, insurance consultants

We need a more professional looking brochure for our managers to be able to leave behind with potential clients they meet with. This brochure needs to summarize all the services and value that The Harbourline Group has to offer, pretty much giving an overview of the company.
The clients we deal with are Funeral Homes and Funeral Directors, we are an organization dedicated to assisting funeral homes in implementing highly profitable insurance programs while providing the training, support and service along the way. More information is provided in the brochure attached.
We are going for a professional simple theme, we want to get the message across without overwhelming the client.
This brochure needs to be a Tri-Fold, Landscaped format.
I have attached our current brochure design as reference and more information about the our company and what we offer. This one is obviously what we are looking to replace, but the information will be generally the same. It needs to be more visually appealing and maybe consolidate some of the information so it's not just a block of text.
Color: We would like to keep the color scheme in the White, Blue, Grey, Black spectrum
I have also attached our logo and Business Card
Target Market(s)
The target market for this brochure will be Funeral Directors and Funeral Homes. This brochure will be left behind with the potential clients as an overview of the services The Harbourline Group has to offer.
Industry/Entity Type
Insurance
Look and feel

```html
<!DOCTYPE html>
<html lang="en">
<head>
<meta charset="utf-8">
<title>The Harbourline Group – Tri-Fold Brochure</title>
<link rel="stylesheet" href="https://fonts.googleapis.com/css2?family=Tinos:wght@400;700&family=Montserrat:wght@400;600&family=Arimo:wght@400&display=swap">
<style>
  :root {
    --blue: #1f7fc4;
    --quote-blue: #2a6fb0;
    --ink: #2b2b2b;
    --white: #ffffff;
    --slate-dark: #3f464d;
    --slate-mid: #5e666e;
    --slate-light: #9aa1a7;
    --mist: #e8eaec;
  }
  * { margin: 0; padding: 0; box-sizing: border-box; }
  html, body { width: 1200px; height: 938px; overflow: hidden; background: var(--white); }
  .brochure { position: relative; width: 1200px; height: 938px; background: var(--white); color: var(--ink); font-family: "Montserrat", Arial, sans-serif; }
  .panel { position: absolute; top: 0; height: 938px; }
  .panel--left { left: 0; width: 399px; }
  .panel--middle { left: 399px; width: 409px; }
  .panel--right { left: 808px; width: 392px; }

  .body-copy { font-size: 16.4px; line-height: 20.6px; color: var(--ink); }
  .body-copy p + p { margin-top: 20px; }
  .body-copy strong { font-weight: 600; }

  /* left */
  .hero-photo { position: absolute; left: 0; top: 0; width: 399px; height: 276px; background: linear-gradient(135deg, #dfe6ec 0%, #b9c6d2 45%, #7d8d9c 100%); }
  .title-serif { font-family: "Tinos", "Times New Roman", serif; color: var(--blue); font-weight: 400; }
  .better-title { position: absolute; left: 0; width: 390px; top: 300px; text-align: center; font-size: 44px; }
  .alt-row { position: absolute; left: 0; top: 362px; width: 399px; height: 34px; }
  .alt-row .rule { position: absolute; top: 17px; height: 2px; background: var(--blue); }
  .alt-row .word { position: absolute; left: 62px; top: 0; font-size: 27px; letter-spacing: 3px; color: var(--blue); background: var(--white); padding: 0 2px; }
  .left-copy { position: absolute; left: 18px; top: 416px; width: 350px; }
  .option-band { position: absolute; left: 0; top: 853px; width: 399px; height: 85px; background: linear-gradient(180deg, #6b7279 0%, var(--slate-dark) 100%); color: var(--white); font-size: 25px; line-height: 30px; text-align: center; padding-top: 14px; letter-spacing: .5px; }

  /* middle */
  .rate-board { position: absolute; left: 0; top: 0; width: 409px; height: 493px; background: linear-gradient(180deg, #4e555c 0%, #6d757c 55%, #565d64 100%); }
  .rate-table { position: absolute; left: 28px; top: 27px; border-collapse: collapse; font-family: "Arimo", Arial, sans-serif; font-size: 12px; color: var(--white); text-align: center; }
  .rate-table td, .rate-table th { border: 2px solid #e6e8ea; font-weight: 400; line-height: 15px; padding: 0 2px; }
  .rate-table .hdr { height: 61px; }
  .rate-table .row { height: 38px; }
  .rate-table .note { height: 41px; font-size: 11.5px; }
  .rule-line { position: absolute; height: 2px; background: var(--blue); }
  .diff-title { position: absolute; left: 0; width: 409px; top: 538px; text-align: center; font-size: 44px; }
  .mid-copy { position: absolute; left: 28px; width: 340px; }
  .pull-quote { position: absolute; left: 41px; top: 724px; width: 300px; font-family: "Tinos", "Times New Roman", serif; color: var(--quote-blue); font-size: 19.5px; line-height: 25.5px; text-align: justify; }

  /* right */
  .offer-title { position: absolute; left: 0; width: 392px; top: 29px; text-align: center; font-size: 47px; }
  .right-copy { position: absolute; left: 28px; width: 350px; }
  .sub-head { position: absolute; left: 28px; font-family: "Tinos", "Times New Roman", serif; font-weight: 700; font-size: 21px; color: var(--blue); }
  .contact-fade { position: absolute; left: 0; top: 742px; width: 392px; height: 30px; background: linear-gradient(180deg, var(--white) 0%, var(--mist) 60%, #c9cdd1 100%); }
  .contact-band { position: absolute; left: 0; top: 772px; width: 392px; height: 66px; background: linear-gradient(180deg, #6d747a 0%, var(--slate-mid) 100%); color: var(--white); text-align: center; font-family: "Tinos", "Times New Roman", serif; font-size: 45px; line-height: 66px; }
  .contact-card { position: absolute; left: 0; top: 841px; width: 392px; height: 97px; background: linear-gradient(180deg, var(--slate-mid) 0%, var(--slate-dark) 100%); color: var(--white); text-align: center; font-family: "Tinos", "Times New Roman", serif; padding-top: 14px; }
  .contact-card .firm { font-size: 20px; font-weight: 700; line-height: 24px; }
  .contact-card .line { font-size: 14px; line-height: 19px; }
</style>
</head>
<body>
<main class="brochure">

  <section class="panel panel--left">
    <div class="hero-photo" role="img" aria-label="Photo of a smiling senior couple meeting with an insurance advisor at a table"></div>
    <h1 class="title-serif better-title">Provide A Better</h1>
    <div class="alt-row">
      <span class="rule" style="left:0;width:62px"></span>
      <span class="rule" style="left:320px;width:50px"></span>
      <span class="word">ALTERNATIVE</span>
    </div>
    <div class="body-copy left-copy">
      <p><strong>Our Final Expense</strong> products provide a better value to your customers by covering every cost associated with their funeral as opposed to being limited with pre-need coverage. Your clients will be able to purchase additional services such as flowers, memoirs, and everything else pre need will not cover.</p>
      <p>Lower monthly payments on the policies allow you to reach a larger number of people who would otherwise not be able to afford the funeral they deserve.</p>
      <p>Because our products have a significantly lower payment schedule compared to pre-need, your clients will have a much easier time making payments reducing the number of lapsed policies.</p>
    </div>
    <div class="option-band">PRE NEED ISN’T THE<br>ONLY OPTION</div>
  </section>

  <section class="panel panel--middle">
    <div class="rate-board">
      <table class="rate-table">
        <colgroup><col style="width:35px"><col style="width:68px"><col style="width:66px"><col style="width:56px"><col style="width:72px"><col style="width:55px"></colgroup>
        <tr class="hdr"><th>Age</th><th>Face Value</th><th>Male Pre Needs 5year</th><th>Final Expense Male</th><th>Female Pre Needs 5year</th><th>Final Expense Femae</th></tr>
        <tr class="row"><td>65</td><td>$10,000</td><td>$230</td><td>$53</td><td>$230</td><td>$41</td></tr>
        <tr class="row"><td>70</td><td>$10,000</td><td>$247</td><td>$68</td><td>$247</td><td>$52</td></tr>
        <tr class="row"><td>75</td><td>$10,000</td><td>$275</td><td>$93</td><td>$275</td><td>$71</td></tr>
        <tr class="row"><td>80</td><td>$10,000</td><td>$422</td><td>$145</td><td>$422</td><td>$103</td></tr>
        <tr class="row"><th>Age</th><th>Pre Needs Single Pay</th><th colspan="2">Final Expense Single Pay Man</th><th colspan="2">Final Expense Single Pay Woman</th></tr>
        <tr class="row"><td>65</td><td>$10,810</td><td colspan="2">$15,545</td><td colspan="2">$17,509</td></tr>
        <tr class="row"><td>70</td><td>$10,526</td><td colspan="2">$13,653</td><td colspan="2">$15,675</td></tr>
        <tr class="row"><td>75</td><td>$10,309</td><td colspan="2">$12,401</td><td colspan="2">$13,664</td></tr>
        <tr class="row"><td>80</td><td>$10,256</td><td colspan="2">$11,238</td><td colspan="2">$12,497</td></tr>
        <tr class="note"><td></td><td></td><td colspan="2">*Rates Subject<br>to change</td><td colspan="2"></td></tr>
      </table>
    </div>
    <span class="rule-line" style="left:0;top:530px;width:409px"></span>
    <h2 class="title-serif diff-title">See the Difference</h2>
    <span class="rule-line" style="left:0;top:595px;width:409px"></span>
    <div class="body-copy mid-copy" style="top:622px"><p>This rate chart above shows the dramatic contrast between expensive pre-need payments and our cheaper alternative option.</p></div>
    <blockquote class="pull-quote">“A typical pre need payment is about the same as car payment, while a final expense payment is closer to a tank of gas”</blockquote>
    <div class="body-copy mid-copy" style="top:850px"><p>Provide a much greater value to your customer giving them options they can afford.</p></div>
  </section>

  <section class="panel panel--right">
    <span class="rule-line" style="left:0;top:24px;width:392px"></span>
    <h2 class="title-serif offer-title">Key Offerings</h2>
    <span class="rule-line" style="left:0;top:89px;width:392px"></span>
    <div class="body-copy right-copy" style="top:120px">
      <p>Provide your clients alternative options for the costs of burial</p>
      <p>We consult with you on maximizing revenue streams from insurance sales and bonuses</p>
      <p>We provide full support and training for all your insurance related needs at no cost to you</p>
    </div>
    <h3 class="sub-head" style="top:367px">Stop leaving business on the table</h3>
    <span class="rule-line" style="left:0;top:401px;width:392px"></span>
    <div class="body-copy right-copy" style="top:415px"><p>By providing a cheaper alternative to Pre Need, you open up the opportunity to help out lower income families that are unable to afford expensive pre need options.</p></div>
    <h3 class="sub-head" style="top:551px">Referral Bonus Program</h3>
    <span class="rule-line" style="left:0;top:584px;width:392px"></span>
    <div class="body-copy right-copy" style="top:600px"><p>Take advantage of our referral bonus program by introducing us to other funeral directors or funeral homes. Your representative will be able to explain this system more</p></div>
    <div class="contact-fade"></div>
    <h2 class="contact-band">Contact Us</h2>
    <address class="contact-card" style="font-style:normal">
      <div class="firm">The Harbourline Group</div>
      <div class="line">(555) 014-2765 &nbsp;|&nbsp; www.harbourlinegroup.com</div>
      <div class="line">contracting@harbourlinegroup.com</div>
    </address>
  </section>

</main>
</body>
</html>
```